Water Bottle Label design for Healthy Lifestyle Restaurant

We are looking for a new water bottle label design for our water bottles. The bottles are the same shape and size as the company "clear spring" . See attached photos of our current label and current bottle. The size of the label should be 4inches x 7 inches. We are looking for a design that matches our brand. If you take a look at www.vorlanbistro.example , you will understand more of the concept that we are. We are hoping for a modern clean design .

Industry/Entity Type

Restaurant

Requirements
Must have
• Logo, instagram and website . Maybe a QR code would be a good idea ?
Nice to have
• Maybe a QR code would be a good idea ?
Should not have
• So much blue in the design

```html
<!DOCTYPE html>
<html lang="en">
<head>
<meta charset="utf-8">
<title>Vorlan Water Bottle Label</title>
<link rel="stylesheet" href="https://fonts.googleapis.com/css2?family=Archivo:wght@800&display=swap">
<style>
  :root {
    --page-bg: #ffffff;
    --label-bg: #f1f1f1;
    --label-shade: #e3e3e4;
    --leaf-soft: #c9dba9;
    --leaf-mid: #a9c97e;
    --brand-green: #5c9a12;
    --ink-grey: #6b6b6d;
    --dot-green: #77a83a;
  }
  html, body {
    margin: 0;
    padding: 0;
    width: 1200px;
    height: 1200px;
    overflow: hidden;
    background: var(--page-bg);
  }
  .canvas {
    position: relative;
    width: 1200px;
    height: 1200px;
  }
  .label {
    position: absolute;
    left: 390px;
    top: 230px;
    width: 420px;
    height: 740px;
    background: var(--label-bg);
    overflow: hidden;
  }
  .label-shapes {
    position: absolute;
    inset: 0;
  }
  .botanical-accent {
    position: absolute;
  }
  .brand-column {
    position: absolute;
    left: 0;
    top: 0;
    width: 740px;
    height: 420px;
    transform-origin: 0 0;
    transform: translate(0, 740px) rotate(-90deg);
  }
  .brand-name {
    position: absolute;
    left: 90px;
    top: 120px;
    margin: 0;
    font-family: "Archivo", "Arial Black", sans-serif;
    font-weight: 800;
    font-size: 118px;
    line-height: 1;
    letter-spacing: 2px;
    color: var(--brand-green);
  }
  .brand-mark {
    position: absolute;
    left: 56px;
    top: 190px;
    width: 22px;
    height: 22px;
    border-radius: 50%;
    background: var(--brand-green);
  }
  .tagline {
    position: absolute;
    left: 92px;
    top: 250px;
    margin: 0;
    font-family: "Archivo", "Arial Black", sans-serif;
    font-weight: 800;
    font-size: 27px;
    letter-spacing: 0.5px;
    color: var(--brand-green);
    white-space: nowrap;
  }
  .tagline .divider {
    color: var(--ink-grey);
    margin: 0 14px;
    font-weight: 800;
  }
</style>
</head>
<body>
<div class="canvas">
  <div class="label">
    <svg class="label-shapes" width="420" height="740" viewBox="0 0 420 740" aria-hidden="true">
      <path d="M0 0 H100 C130 60 110 150 70 210 C40 260 20 300 0 330 Z" fill="var(--leaf-soft)"/>
      <path d="M420 360 C360 420 330 520 320 600 C312 660 310 700 300 740 H420 Z" fill="var(--label-shade)"/>
    </svg>
    <div class="botanical-accent" role="img" aria-label="Light green leaf outlines and scattered dots"
         style="left:20px; top:300px; width:90px; height:280px; background:linear-gradient(180deg, rgba(169,201,126,0.35), rgba(170,170,170,0.25)); border-radius:40px;"></div>
    <div class="botanical-accent" role="img" aria-label="Green scattered dots and leaf outline"
         style="left:325px; top:30px; width:70px; height:290px; background:linear-gradient(180deg, rgba(119,168,58,0.45), rgba(169,201,126,0.2)); border-radius:35px;"></div>
    <div class="brand-column">
      <span class="brand-mark"></span>
      <h1 class="brand-name">VORLAN</h1>
      <p class="tagline">HEALTHY KITCHEN<span class="divider">|</span>MEAL PREP</p>
    </div>
  </div>
</div>
</body>
</html>
```